WordPress Direct-Booking Website for Bend, Oregon Vacation Rental — $750 Budget
Project Overview

We are looking for a talented WordPress designer/developer to create a clean, professional and inviting direct-booking website for Cedar Lantern Retreat, an established short-term vacation rental in Bend, Oregon.

The property is currently successfully listed on Stayvora and Hearthlist. Our Stayvora property has approximately a 4.98-star rating with more than 200 reviews, is an Stayvora Visitor Pick, and ranks among the Top 1% of eligible homes.

Project Budget: $750

We will select the designer based on the quality of the initial concept, understanding of the property, proposed booking solution and ability to deliver a completed and functioning WordPress website.

Existing Stayvora Listing

Please use our current Stayvora listing as the primary reference for photographs, property details, amenities and design inspiration:

https://www.stayvora-example.com/rooms/48172635

Original high-resolution photographs and additional property information will be provided to the selected designer.

Design Direction

We want the website to feel:

Upscale but comfortable
Warm and welcoming
Clean and uncluttered
Pacific Northwest / Central Oregon
Professional rather than corporate
Highly visual with large property photographs
Easy to navigate
Excellent on phones, tablets and desktop computers

We welcome creativity and want designers to show us their vision for the property rather than simply copying our Stayvora listing.

The website should immediately communicate that Cedar Lantern Retreat is a highly rated vacation rental in an excellent Bend location.

Key Property Features
3 bedrooms
2 bathrooms
Sleeps up to 6 guests
Pet friendly
Approximately a 5-minute walk to Bend's Tannery Row Quarter
Near restaurants, shopping and Larkspur Fields Pavilion
Private fenced backyard
Covered outdoor area
Off-street driveway parking
Fireplace
Well-equipped kitchen
Stayvora Prime Keeper
Stayvora Visitor Pick
Top 1% of eligible Stayvora homes
Approximately 4.98 stars with 200+ guest reviews

Our location, guest reviews, cleanliness, comfort, backyard, pet-friendly accommodations and walkability should be major selling points throughout the website.

Website Structure

We anticipate approximately 6–7 pages:

Home

Large hero photograph with a strong opening message and prominent BOOK DIRECT and CHECK AVAILABILITY buttons.

The home page should quickly communicate:

CEDAR LANTERN RETREAT — BEND, OREGON

3 Bedrooms | 2 Baths | Sleeps 6 | Pet Friendly | Walk to Tannery Row

Our exceptional guest rating and Stayvora history should also be prominently featured.

The House

Bedrooms, bathrooms, kitchen, living areas, backyard and major amenities.

Photo Gallery

Large, attractive and fast-loading photographs with an easy-to-use mobile gallery.

Location / Explore Bend

Tannery Row Quarter, Larkspur Fields Pavilion, Deschutes River, restaurants, breweries, shopping, downtown Bend and nearby outdoor recreation.

Guest Reviews

Selected guest reviews and prominent presentation of our strong Stayvora reputation.

Availability & Book Direct

A simple and professional direct-booking experience.

Contact / FAQ

Contact information plus common questions regarding pets, parking, check-in/check-out, cancellations and other policies.

IMPORTANT — Direct Booking & Credit Card Requirements

We want guests to be able to book directly through the website without having to contact us first.

The website should use a proven WordPress vacation-rental booking plugin or system rather than a custom-built reservation/payment system.

Guests should be able to:

Select arrival and departure dates
See available dates
Enter number of guests
See nightly charges
See cleaning fees
See applicable lodging taxes and other charges
See the complete reservation total before paying
Enter guest/contact information
Pay securely by credit or debit card
Receive an automatic reservation confirmation

Paylume is our preferred credit-card processor.

Credit-card information must be processed securely through Paylume or another established payment processor. Credit-card information should NOT be stored directly on our WordPress website.

Stayvora & Hearthlist Calendar Synchronization

This is very important.

The direct-booking calendar must synchronize with our existing Stayvora and Hearthlist calendars to reduce the possibility of double bookings.

For this single-property website, we prefer a simple solution using Stayvora/Hearthlist calendar or iCal synchronization rather than an expensive monthly channel-management service, if practical.

The designer should clearly identify the booking plugin/system they propose using.

IMPORTANT — Tell Us Your Proposed Booking Solution

As part of your submission, please tell us:

Which WordPress booking plugin/system you recommend.
Whether it synchronizes availability with Stayvora and Hearthlist.
Whether it integrates directly with Paylume.
The initial cost of the plugin/software.
Any annual or monthly fees.
Whether any additional paid software or services will be required.

We strongly prefer a solution with little or no ongoing monthly software expense.

We do not want to select a designer and later discover that the proposed booking system requires an expensive monthly subscription.

WordPress & Technical Requirements

The completed project should include:

Fully functioning WordPress website
Responsive desktop/tablet/mobile design
Fast-loading pages
Optimized photographs
SSL/HTTPS compatibility
Direct-booking functionality
Paylume payment integration
Stayvora calendar synchronization
Hearthlist calendar synchronization
Automatic booking confirmations
Cleaning fee and lodging-tax calculations
Contact form
Terravue Maps/location integration
Basic spam/security protection
Terravue Metrics capability
Basic SEO setup
Search-engine submission capability
Easy owner editing of text, rates and photographs
Search Engine Optimization

The website should be structured for Terravue and other search engines.

Important search themes include:

Bend Oregon vacation rental
Bend Oregon vacation home
Tannery Row Quarter vacation rental
Vacation rental near Tannery Row Bend
Bend Oregon pet-friendly vacation rental
Bend vacation rental near Larkspur Fields Pavilion
Bend Oregon direct booking vacation rental

We are not expecting an extensive ongoing SEO campaign for the $750 project. We do expect proper page titles, descriptions, headings, image optimization and a good technical foundation for future SEO.

Ownership

Upon completion and final payment:

We own the completed WordPress website.
We receive full WordPress administrator access.
We control the domain and hosting accounts.
We own all custom design files created for the project.
All necessary login credentials are provided to us.
The website can be moved to another WordPress hosting provider in the future.
There should be no proprietary dependency on the developer after completion.
What We Want From Contestants

Please review our Stayvora listing before submitting your concept.

We are particularly interested in seeing an initial homepage concept showing how you would present:

Cedar Lantern Retreat
The Bend / Tannery Row location
Our photography
Our exceptional guest reviews and ratings
The Book Direct message
The availability/booking call-to-action

We will provide feedback on the concepts we like and work with the selected designer to refine and complete the website.

Our Goal

Our objective is straightforward:

Create a beautiful, trustworthy and easy-to-use website that encourages guests to book Cedar Lantern Retreat directly with us.

The website will complement—not replace—our existing Stayvora and Hearthlist listings.

We want repeat guests and new customers to have an easy way to find the property, check availability and book directly while receiving the same professional experience they expect from a major vacation-rental platform.

Target Market(s)

Consumers looking to to travel to Mexico for vacation. Family or couples

Industry/Entity Type

Short term vacation rental industry

Coding

Coded - Design and coding required

Number of Pages Required

5+ page

Requirements
Must have
• Capabilities to accept credit card payments and link to other rental property sites calendars such as LODGIX and Stayvorra
Nice to have
• Option for best plugins for property rental

```html
<!DOCTYPE html>
<html lang="en">
<head>
<meta charset="utf-8">
<title>Explore Bend · Cedar Lantern Retreat</title>
<link rel="stylesheet" href="https://fonts.googleapis.com/css2?family=Fraunces:opsz,wght@9..144,500;9..144,600&family=Inter:wght@400;500;600;700&display=swap">
<style>
:root{
  --cream:#faf6ef;
  --sand:#f3ece2;
  --card:#fffdf9;
  --ink:#2a2520;
  --muted:#6d655c;
  --faint:#9a9187;
  --rust:#b5552a;
  --rust-soft:#f4e3d8;
  --pill:#efeae2;
  --forest:#2f3b2d;
  --forest-line:#45513f;
  --forest-text:#d9dccf;
  --serif:"Fraunces", Georgia, serif;
  --sans:"Inter", Arial, sans-serif;
}
*{box-sizing:border-box;margin:0;padding:0}
html,body{width:1200px;height:4135px;overflow:hidden}
body{background:var(--cream);font-family:var(--sans);color:var(--ink)}
a{color:inherit;text-decoration:none}
.wrap{width:966px;margin:0 auto}

/* header */
.site-header{height:50px;background:var(--cream);display:flex;align-items:center;justify-content:space-between;padding:0 117px}
.brand-name{font-family:var(--serif);font-weight:600;font-size:16px;line-height:1}
.brand-sub{font-size:7.5px;letter-spacing:2.6px;color:var(--rust);font-weight:600;margin-top:5px}
.main-nav{display:flex;gap:27px;font-size:11.5px;font-weight:500;margin-left:-40px}
.main-nav .active{color:var(--rust);border-bottom:1.5px solid var(--rust);padding-bottom:4px}
.header-actions{display:flex;align-items:center;gap:10px;font-size:11.5px;font-weight:500}
.header-actions svg{width:12px;height:12px}
.btn{display:inline-flex;align-items:center;gap:6px;background:var(--rust);color:#fff;border-radius:999px;font-weight:700;letter-spacing:.6px;text-transform:uppercase}
.btn-small{font-size:9px;padding:9px 14px;margin-left:6px}

/* hero */
.hero{height:375px;position:relative;background:linear-gradient(160deg,#5f6a4c 0%,#6d6250 35%,#4f5a48 60%,#6b7a86 80%,#8a8276 100%)}
.hero::after{content:"";position:absolute;inset:0;background:linear-gradient(90deg,rgba(25,22,18,.72) 0%,rgba(25,22,18,.45) 45%,rgba(25,22,18,.15) 100%)}
.hero-copy{position:absolute;left:117px;top:143px;z-index:1;color:#fff}
.eyebrow{font-size:9px;letter-spacing:3px;font-weight:600;color:var(--rust);text-transform:uppercase}
.hero h1{font-family:var(--serif);font-weight:500;font-size:48px;line-height:51px;margin-top:20px}
.hero p{font-size:14px;line-height:23px;color:rgba(255,255,255,.85);margin-top:20px;width:470px}

/* explore */
.explore{padding:70px 0 64px}
.group + .group{margin-top:60px}
.group-head{display:flex;align-items:center;gap:13px;height:40px;margin-bottom:28px}
.group-icon{width:38px;height:38px;border-radius:10px;background:var(--rust-soft);display:flex;align-items:center;justify-content:center}
.group-icon svg{width:16px;height:16px;stroke:var(--rust);fill:none;stroke-width:1.7;stroke-linecap:round;stroke-linejoin:round}
.group-title{font-family:var(--serif);font-weight:500;font-size:24px;line-height:1}
.group-sub{font-size:11px;color:var(--muted);margin-top:4px}
.place{display:flex;height:var(--h,165px);background:var(--card);border-radius:12px;overflow:hidden;box-shadow:0 2px 10px rgba(60,40,20,.09)}
.place + .place{margin-top:20px}
.place-photo{width:238px;flex:none}
.place-body{padding:24px 24px 0 22px}
.place-meta{display:flex;align-items:center;gap:10px;font-size:8.5px;letter-spacing:1.4px;text-transform:uppercase;color:var(--faint);font-weight:500}
.place-tag{background:var(--pill);color:var(--muted);font-weight:700;border-radius:999px;padding:4px 8px}
.place h3{font-family:var(--serif);font-weight:500;font-size:19.5px;margin-top:12px}
.place p{font-size:11.5px;line-height:19px;color:#4e4740;margin-top:10px;max-width:690px}

/* map */
.bearings{background:var(--sand);padding:67px 0 62px}
.bearings h2{font-family:var(--serif);font-weight:500;font-size:36px;margin-top:12px}
.bearings .lead{font-size:14px;line-height:24px;color:#4e4740;width:540px;margin-top:12px}
.map-card{margin-top:40px;height:583px;background:var(--card);border-radius:14px;overflow:hidden;box-shadow:0 3px 14px rgba(60,40,20,.1)}
.map-area{height:541px;position:relative;background:linear-gradient(135deg,#ece6dc 0%,#f1e3dc 40%,#e9dfe4 70%,#e4e9dc 100%)}
.map-zoom{position:absolute;right:10px;top:10px;width:22px;background:#fff;border:1px solid #cfc8bd;border-radius:3px;font-size:14px;text-align:center;line-height:21px;color:#333}
.map-zoom span{display:block}
.map-zoom span + span{border-top:1px solid #ddd}
.map-strip{height:42px;display:flex;align-items:center;justify-content:space-between;padding:0 22px;font-size:11px;color:var(--muted)}
.map-strip .where{display:flex;align-items:center;gap:6px}
.map-strip svg{width:12px;height:12px;stroke:var(--rust);fill:none;stroke-width:1.8}
.map-strip .open{color:var(--rust);font-weight:600}

/* cta */
.closing{height:327px;text-align:center;padding-top:68px}
.closing h2{font-family:var(--serif);font-weight:500;font-size:30px;line-height:37px}
.closing p{font-size:12.5px;line-height:20px;color:#4e4740;margin-top:18px}
.btn-large{font-size:11px;padding:13px 26px;margin-top:22px;box-shadow:0 4px 12px rgba(181,85,42,.3)}

/* footer */
.site-footer{height:367px;background:var(--forest);color:var(--forest-text);padding-top:58px}
.footer-cols{display:grid;grid-template-columns:297px 223px 223px 223px;height:230px}
.site-footer .brand-name{color:#fff;font-size:18px}
.site-footer .brand-sub{color:#b8bdae}
.footer-about{font-size:11px;line-height:18px;margin-top:20px;width:260px}
.footer-rating{font-size:9px;margin-top:18px;line-height:20px;width:230px}
.footer-rating b{color:#e0a24a;font-weight:400}
.footer-head{font-size:8.5px;letter-spacing:2.4px;text-transform:uppercase;color:#a9af9e;font-weight:600;margin-bottom:14px;margin-top:2px}
.footer-list{list-style:none;font-size:11px;line-height:24px}
.footer-contact{font-size:11px;line-height:24px}
.footer-contact .addr{line-height:18px;color:#b8bdae;margin-top:8px}
.footer-contact svg{width:11px;height:11px;stroke:currentColor;fill:none;stroke-width:1.8;vertical-align:-1px;margin-right:6px}
.btn-footer{font-size:10px;padding:13px 22px;margin-top:22px}
.footer-base{border-top:1px solid var(--forest-line);display:flex;justify-content:space-between;padding-top:22px;font-size:9.5px;color:#a9af9e}
.footer-base nav{display:flex;gap:20px}
</style>
</head>
<body>

<header class="site-header">
  <div class="brand">
    <div class="brand-name">Cedar Lantern Retreat</div>
    <div class="brand-sub">BEND · OREGON</div>
  </div>
  <nav class="main-nav">
    <a href="#">The House</a><a href="#">Gallery</a><a href="#" class="active">Explore Bend</a><a href="#">Reviews</a><a href="#">Book Direct</a>
  </nav>
  <div class="header-actions">
    <svg viewBox="0 0 24 24" fill="none" stroke="currentColor" stroke-width="2"><path d="M5 3h4l2 5-3 2a12 12 0 0 0 6 6l2-3 5 2v4a2 2 0 0 1-2 2A17 17 0 0 1 3 5a2 2 0 0 1 2-2z"/></svg>
    <span>(541) 555-0188</span>
    <a href="#" class="btn btn-small">Book Direct →</a>
  </div>
</header>

<section class="hero" role="img" aria-label="Aerial view of Bend with the river curving past the neighborhood">
  <div class="hero-copy">
    <div class="eyebrow">Explore Bend</div>
    <h1>The town the<br>house lives in</h1>
    <p>A local's shortlist, sorted by how far you'll need to walk — which, from Cedar Lantern Retreat, is usually not far at all.</p>
  </div>
</section>

<main class="explore">
  <div class="wrap">

    <section class="group">
      <div class="group-head">
        <div class="group-icon"><svg viewBox="0 0 24 24"><path d="M8 4c2 0 3 3 3 6s-1 4-3 4-3-2-3-5 1-5 3-5zM6 17h4v2a2 2 0 0 1-4 0zM16 7c2 0 3 2 3 5s-1 5-3 5-3-1-3-4 1-6 3-6zM14 19h4v1a2 2 0 0 1-4 0z"/></svg></div>
        <div><div class="group-title">By Foot</div><div class="group-sub">Under 15 minutes from the front door</div></div>
      </div>

      <article class="place" style="--h:164px">
        <div class="place-photo" role="img" aria-label="Aerial photo of the Tannery Row Quarter" style="background:linear-gradient(180deg,#4f8ac6 0%,#7d8f78 35%,#6f7d5a 100%)"></div>
        <div class="place-body">
          <div class="place-meta"><span class="place-tag">5 min walk</span>Shopping, dining &amp; river trails at Bend's front porch</div>
          <h3>Tannery Row Quarter</h3>
          <p>Bend's most beloved district — converted mill buildings wrapped by the Deschutes, with 40+ shops, a riverside promenade and the best people-watching in Central Oregon. Morning runs, evening strolls, everything in between. You'll know the smokestacks by the end of the week.</p>
        </div>
      </article>

      <article class="place" style="--h:236px">
        <div class="place-photo" role="img" aria-label="Sunset over the riverside outdoor pavilion" style="background:linear-gradient(180deg,#e7a12f 0%,#d9641d 35%,#7a3b22 60%,#3f3a33 100%)"></div>
        <div class="place-body">
          <div class="place-meta"><span class="place-tag">9 min walk</span>World-class shows on the river — walk home after</div>
          <h3>Larkspur Fields Pavilion</h3>
          <p>Central Oregon's premier outdoor venue, tucked into the pines along the Deschutes. Touring legends and summer residencies, all within a nine-minute stroll of your front door — which means no parking scramble, no post-show traffic. Just walk out with the crowd thinned and be home before the encore echoes fade.</p>
        </div>
      </article>

      <article class="place" style="--h:177px">
        <div class="place-photo" role="img" aria-label="Floating the river on an inner tube" style="background:linear-gradient(180deg,#8fb7df 0%,#5d86a6 45%,#2f5a78 100%)"></div>
        <div class="place-body">
          <div class="place-meta"><span class="place-tag">4 min walk</span>The mile of river that defines the neighborhood</div>
          <h3>Deschutes River Trail</h3>
          <p>Access the Deschutes River Trail at the foot of the district and follow it through town — runners, floaters, herons, otters. In summer, rent tubes and drift the Bend stretch; the takeout is a short walk back to the house. Towels are in the hall closet.</p>
        </div>
      </article>
    </section>

    <section class="group">
      <div class="group-head">
        <div class="group-icon"><svg viewBox="0 0 24 24"><circle cx="6" cy="16" r="3.5"/><circle cx="18" cy="16" r="3.5"/><path d="M6 16l4-7h5l3 7M10 9l2 7"/></svg></div>
        <div><div class="group-title">A Short Ride</div><div class="group-sub">5–15 minutes by car or bike</div></div>
      </div>

      <article class="place">
        <div class="place-photo" role="img" aria-label="Downtown restaurant front lit up at night" style="background:linear-gradient(180deg,#1d1a1e 0%,#7a2a1c 45%,#c0452a 70%,#3a2a22 100%)"></div>
        <div class="place-body">
          <div class="place-meta"><span class="place-tag">8 min drive</span>Minnesota Street's restaurants, galleries &amp; nightlife</div>
          <h3>Downtown Bend</h3>
          <p>Historic downtown has the city's best concentration of dinner spots, wine bars and independent shops. Start at a rooftop for sunset, end at a late-night slice. Drake Park and Mirror Pond — postcard Bend — anchor the west end.</p>
        </div>
      </article>

      <article class="place" style="--h:167px">
        <div class="place-photo" role="img" aria-label="Brewery building with flower gardens under blue sky" style="background:linear-gradient(180deg,#3d7fd0 0%,#8ab0d6 40%,#6f8a5a 70%,#a7683a 100%)"></div>
        <div class="place-body">
          <div class="place-meta"><span class="place-tag">5–10 min</span>The most breweries per capita in Oregon</div>
          <h3>Bend Brew Loop</h3>
          <p>Nearly 30 breweries in one small city — and the house sits between two of the best corridors. Cascadia Brewing's original public house and the Eastside brewery cluster (Ridgeline, Juniper Hollow, Basalt Keg, Pinecrest) are all minutes away. A stamp card is a fun way to work through them.</p>
        </div>
      </article>

      <article class="place" style="--h:167px">
        <div class="place-photo" role="img" aria-label="Coffee cup and pastries in a cozy café" style="background:linear-gradient(160deg,#6a4a33 0%,#8c6a4c 40%,#4d5e4a 70%,#2f2a24 100%)"></div>
        <div class="place-body">
          <div class="place-meta"><span class="place-tag">5 min</span>A serious coffee town</div>
          <h3>Coffee &amp; Breakfast</h3>
          <p>Bend takes mornings personally — Lumen, Highmark, Kettlebird and a dozen other roasters and bakeries compete for your first hour. Our welcome guide lists the current favorites, with the local's order at each.</p>
        </div>
      </article>
    </section>

    <section class="group">
      <div class="group-head">
        <div class="group-icon"><svg viewBox="0 0 24 24"><path d="M3 19l7-12 4 6 2-3 5 9z"/></svg></div>
        <div><div class="group-title">The Big Outdoors</div><div class="group-sub">Within an hour — the reason you're here</div></div>
      </div>

      <article class="place" style="--h:176px">
        <div class="place-photo" role="img" aria-label="Tall pines along a forest trail" style="background:linear-gradient(180deg,#3e78c2 0%,#5a6f4a 45%,#6b5236 75%,#3c3a26 100%)"></div>
        <div class="place-body">
          <div class="place-meta"><span class="place-tag">15–30 min</span>Hundreds of trailheads out the front door</div>
          <h3>Trails &amp; Lakes</h3>
          <p>Shevlin Park, the west-side singletrack (mountain biking's holy ground), the national forest and dozens of alpine lakes — all within a half hour. The gear closet has daypacks and trail guides; the drying rack handles whatever the day does to you.</p>
        </div>
      </article>

      <article class="place" style="--h:165px">
        <div class="place-photo" role="img" aria-label="Aerial view toward the Cascade peaks" style="background:linear-gradient(180deg,#5a92cf 0%,#8b9b8a 35%,#6d7760 100%)"></div>
        <div class="place-body">
          <div class="place-meta"><span class="place-tag">25–40 min</span>Ski, snowboard or lake-day, same highway</div>
          <h3>Cascade Lakes &amp; Mt. Corvallo</h3>
          <p>The Cascade Lakes Highway is a choose-your-own-adventure: 3,700 skiable acres in winter; Sparks, Elk and Cultus lakes in summer. The house stores your skis, boards and bikes by the entry — and boot dryers mean warm feet.</p>
        </div>
      </article>

      <article class="place" style="--h:166px">
        <div class="place-photo" role="img" aria-label="Paddleboard on a calm forest lake" style="background:linear-gradient(180deg,#8cb4dc 0%,#3f6a48 40%,#2f4b3e 65%,#6b8ea6 100%)"></div>
        <div class="place-body">
          <div class="place-meta"><span class="place-tag">10 min</span>Float, paddle, fish — the Deschutes is yours</div>
          <h3>On the Water</h3>
          <p>The river through town is a slow, friendly float in summer; upstream is trout water. Outfitters rent SUPs and tubes near the house, and several put-ins are minutes away by car or bike.</p>
        </div>
      </article>
    </section>

  </div>
</main>

<section class="bearings">
  <div class="wrap">
    <div class="eyebrow">Find your bearings</div>
    <h2>One dot, endless options</h2>
    <p class="lead">The house sits on a quiet residential lane with the Tannery Row Quarter at the end of the street — the river trail, the amphitheater and half of Bend's best evenings within a short walk.</p>
    <div class="map-card">
      <div class="map-area" role="img" aria-label="Street map of Bend with the house marked near the Tannery Row Quarter">
        <div class="map-zoom"><span>+</span><span>−</span></div>
      </div>
      <div class="map-strip">
        <span class="where"><svg viewBox="0 0 24 24"><path d="M12 21s-7-6.5-7-12a7 7 0 0 1 14 0c0 5.5-7 12-7 12z"/><circle cx="12" cy="9" r="2.5"/></svg>Near SE Alder Crest Rd &amp; Birch St · Bend's Tannery Row Quarter</span>
        <a href="#" class="open">Open in maps ↗</a>
      </div>
    </div>
  </div>
</section>

<section class="closing">
  <h2>The best of Bend, five<br>minutes from the front door</h2>
  <p>Stay where the location does half the vacation planning for you —<br>and the calendar is live right now.</p>
  <a href="#" class="btn btn-large">Check Availability &nbsp;→</a>
</section>

<footer class="site-footer">
  <div class="wrap">
    <div class="footer-cols">
      <div>
        <div class="brand-name">Cedar Lantern Retreat</div>
        <div class="brand-sub">BEND · OREGON</div>
        <p class="footer-about">A warm, professionally managed vacation home a five-minute walk from the Tannery Row Quarter — for slow mornings, river afternoons and fireside evenings.</p>
        <p class="footer-rating"><b>★</b> 4.98 · 205 reviews &nbsp;•&nbsp; Prime Keeper &nbsp;•&nbsp; Visitor Pick</p>
      </div>
      <div>
        <div class="footer-head">Explore</div>
        <ul class="footer-list"><li>Home</li><li>The House</li><li>Gallery</li><li>Explore Bend</li><li>Reviews</li><li>Book Direct</li><li>Contact &amp; FAQ</li></ul>
      </div>
      <div>
        <div class="footer-head">The Stay</div>
        <ul class="footer-list"><li>3 bedrooms · 2 baths · sleeps 6</li><li>Pet friendly (2 dogs)</li><li>Check-in 4 PM · check-out 10 AM</li><li>Free driveway parking</li><li>Fast WiFi</li></ul>
      </div>
      <div class="footer-contact">
        <div class="footer-head">Book &amp; Contact</div>
        <div><svg viewBox="0 0 24 24"><path d="M5 3h4l2 5-3 2a12 12 0 0 0 6 6l2-3 5 2v4a2 2 0 0 1-2 2A17 17 0 0 1 3 5a2 2 0 0 1 2-2z"/></svg>(541) 555-0188</div>
        <div>stay@cedarlanternretreat.com</div>
        <div class="addr">Near SE Alder Crest Rd &amp; Birch St ·<br>Bend's Tannery Row Quarter</div>
        <a href="#" class="btn btn-footer">Check Availability &nbsp;→</a>
      </div>
    </div>
    <div class="footer-base">
      <span>© 2026 Cedar Lantern Retreat · Bend, Oregon. All rights reserved.</span>
      <nav><a href="#">House rules</a><a href="#">Cancellation policy</a><span>Calendar synced with Stayvora &amp; Hearthlist</span></nav>
    </div>
  </div>
</footer>

</body>
</html>
```